"Landing Page Design for Premium Eco-Friendly Laundry Strips – Plooifris.nl"

We need a visually appealing and high-converting landing page for our premium laundry strips, emphasizing luxury, sustainability, and ease of use. The page should include sections such as:

Hero Section: A compelling introduction with a strong headline, subheadline, and a clear call-to-action (CTA).
Product Benefits: Highlighting key features like eco-friendliness, long-lasting scent, and hypoallergenic qualities.
Product Description: Focusing on innovation and sustainability.
How It Works: Simple, visual steps for using the product.
Customer Reviews: Authentic testimonials to build trust and social proof.
FAQ Section: Addressing common concerns about the product.
The design should maintain a luxurious aesthetic while ensuring clarity and user-friendliness. We also offer free shipping on all orders, a key differentiator to be prominently displayed. All texts and translations are already provided for implementation. Please deliver the design in Figma format."

Target Market(s)

"Eco-conscious consumers and families seeking premium and sustainable laundry solutions. Target age group: 25-50, predominantly women who prioritize luxury and environmental impact."

Industry/Entity Type

"Laundry care and eco-friendly consumer goods."

Coding

Requirements
Must have
• A visually luxurious design emphasizing premium quality and eco-friendliness. Clear call-to-actions (e.g., 'Try Now – Free Shipping'). Sections for product benefits, how it works, customer reviews, and FAQ. Highlight free shipping with no minimum order prominently."
Nice to have
• Elegant, minimalist animations to enhance the premium feel. Subtle use of gold and black to emphasize luxury, with a touch of green for sustainability. Interactive customer reviews section (e.g., carousel or testimonials)."
Should not have
• Overly cluttered designs or overwhelming text blocks. Generic stock photos not aligned with our brand identity. Bright or overly playful color schemes that detract from the premium feel."

```html
<!DOCTYPE html>
<html lang="nl">
<head>
<meta charset="utf-8">
<title>Plooifris Wasstrips</title>
<link href="https://fonts.googleapis.com/css2?family=Mulish:wght@400;500;600;700;800;900&display=swap" rel="stylesheet">
<style>
:root{
  --bg:#1d1c14;
  --bg-deep:#0c0b08;
  --gold:#c9a13c;
  --gold-light:#e2bd55;
  --gold-btn:#c69c3d;
  --text:#f1ece0;
  --text-soft:#d9d3c4;
  --card:#c8a040;
}
*{margin:0;padding:0;box-sizing:border-box}
html,body{width:1200px;height:4357px;overflow:hidden}
body{
  position:relative;font-family:"Mulish",sans-serif;color:var(--text);
  background:
    radial-gradient(ellipse 420px 380px at 340px 1120px,rgba(150,115,30,.28),transparent 70%),
    radial-gradient(ellipse 380px 420px at 860px 1700px,rgba(150,115,30,.25),transparent 70%),
    radial-gradient(ellipse 520px 300px at 600px 2520px,rgba(150,115,30,.25),transparent 70%),
    var(--bg);
}
.abs{position:absolute}
.hero-bg{left:0;top:0;width:1200px;height:700px}
.header-logo{left:127px;top:36px;display:flex;align-items:center;gap:16px;color:var(--gold);font-weight:700;font-size:22px;letter-spacing:1px}
.header-logo .dot{width:50px;height:50px;border-radius:50%;background:var(--gold)}
.contact{display:flex;align-items:center;gap:10px;font-weight:700;font-size:23px;color:#fff}
.contact svg{width:28px;height:28px}
.header-contacts{right:123px;top:36px;display:flex;gap:22px}
.product-box{background:linear-gradient(160deg,#f4efe2 0%,#f4efe2 30%,#1a1812 45%,#0e0d0a 100%);border-left:16px solid var(--gold);box-shadow:0 10px 40px rgba(0,0,0,.5)}
.hero-box{left:205px;top:130px;width:290px;height:440px}
.hero-title{left:695px;top:112px;width:400px;font-size:43px;font-weight:800;line-height:1.1;color:var(--gold-light)}
.hero-sub{left:697px;top:274px;width:380px;font-size:19.5px;line-height:1.55;color:#fff}
.btn{display:flex;align-items:center;justify-content:center;background:var(--gold-btn);color:#fff;font-weight:700;font-size:16px;box-shadow:0 4px 10px rgba(0,0,0,.3)}
.hero-btn{left:697px;top:413px;width:358px;height:49px}
.section-title{font-size:42px;font-weight:800;line-height:1.2;color:var(--gold-light)}
.why-title{left:125px;top:745px;width:560px}
.ornament{left:130px;top:915px;width:430px;height:430px;border-radius:50%;background:radial-gradient(circle,#f0c95a 0%,#c99432 55%,rgba(29,28,20,0) 72%)}
.features{left:585px;top:895px;width:520px}
.feature{display:flex;gap:14px;height:77px}
.feature .ico{width:38px;height:38px;flex:none;display:flex;align-items:flex-start;justify-content:center}
.feature h3{font-size:17px;font-weight:700;color:var(--gold-light);margin-bottom:4px}
.feature p{font-size:16.5px;color:var(--text-soft)}
.future-title{left:125px;top:1522px;width:500px}
.future-text{left:125px;top:1643px;width:530px;font-size:20px;line-height:1.72;color:var(--text-soft);letter-spacing:.3px}
.future-box{left:707px;top:1492px;width:285px;height:437px}
.steps-title{left:0;top:2060px;width:1200px;text-align:center}
.steps{left:130px;top:2140px;width:920px;display:flex}
.step{flex:1;padding-left:4px}
.step + .step{border-left:2px solid rgba(201,161,60,.35);padding-left:34px}
.step .num{font-size:118px;font-weight:900;color:var(--gold);line-height:1;letter-spacing:-2px;display:flex;align-items:center;gap:14px}
.step .num i{display:block;width:5px;height:110px;background:var(--gold)}
.step p{margin-top:14px;width:150px;font-size:18px;line-height:1.35;color:var(--text-soft)}
.step{height:250px}
.shop-btn{left:451px;top:2445px;width:264px;height:50px}
.reviews-title{left:0;top:2592px;width:1200px;text-align:center}
.review{top:2680px;width:463px;height:251px;border-radius:30px;background:var(--card);padding:52px 50px 0 85px;color:#fff}
.review .q{position:absolute;width:40px;height:30px}
.review blockquote{font-size:24px;line-height:1.38;font-weight:500}
.review cite{display:block;margin-top:18px;font-style:normal;font-weight:800;font-size:21px}
.r1{left:124px}.r2{left:613px}
.faq-title{left:0;top:3030px;width:1200px;text-align:center}
.faq{left:166px;top:3112px;width:869px;height:313px;border:3px solid var(--gold);border-radius:30px;box-shadow:0 12px 0 #050504;padding-top:38px;background:var(--bg)}
.faq-row{display:flex;justify-content:space-between;align-items:center;height:78px;padding:0 48px 0 50px;font-size:23px;color:#fff}
.faq-row + .faq-row{border-top:1px solid rgba(255,255,255,.3)}
.plus{width:48px;height:44px;background:var(--gold);color:#fff;font-size:32px;display:flex;align-items:center;justify-content:center;font-weight:600}
.faq-btn{left:408px;top:3474px;width:384px;height:51px}
.cta-title{left:0;top:3660px;width:1200px;text-align:center;font-size:38px}
.cta-btn{left:455px;top:3850px;width:290px;height:52px}
.socials{left:0;top:4085px;width:1200px;display:flex;justify-content:center;align-items:center;gap:0}
.socials span{width:44px;height:44px;border-radius:50%;background:var(--gold);margin:0 30px}
.socials b{width:1px;height:40px;background:rgba(201,161,60,.35)}
.footer-contacts{left:0;top:4146px;width:1200px;display:flex;justify-content:center;gap:36px}
.copyright{left:0;top:4213px;width:1200px;text-align:center;font-size:14px;color:#fff}
.copyright em{font-style:normal;color:var(--gold)}
</style>
</head>
<body>

<svg class="abs hero-bg" viewBox="0 0 1200 700" aria-hidden="true">
  <polygon points="0,0 1200,0 1200,520 200,680 0,528" fill="#0c0b08"/>
  <polyline points="0,528 200,680 1200,520" fill="none" stroke="#c9a13c" stroke-width="14"/>
</svg>

<div class="abs header-logo"><span class="dot"></span>PLOOIFRIS</div>
<div class="abs header-contacts">
  <div class="contact"><svg viewBox="0 0 24 24" fill="none" stroke="#c9a13c" stroke-width="1.6"><path d="M5 3h4l2 5-2.5 1.5a11 11 0 0 0 6 6L16 13l5 2v4a2 2 0 0 1-2 2A16 16 0 0 1 3 5a2 2 0 0 1 2-2z"/></svg>+31 20 555 0142</div>
  <div class="contact"><svg viewBox="0 0 24 24" fill="none" stroke="#c9a13c" stroke-width="1.6"><rect x="2" y="5" width="20" height="14" rx="1.5"/><path d="M2 6l10 7 10-7"/></svg>info@plooifris.nl</div>
</div>

<div class="abs product-box hero-box" role="img" aria-label="Verpakking Plooifris wasstrips, 100 wasbeurten"></div>
<h1 class="abs hero-title">Ervaar Luxe en Duurzaamheid in Elke Wasbeurt</h1>
<p class="abs hero-sub">Ontdek de premium wasstrips van Plooifris – waar verfijning en ecologisch bewustzijn samenkomen</p>
<a class="abs btn hero-btn">Probeer Nu – Altijd Gratis Verzending!</a>

<h2 class="abs section-title why-title">Waarom Kiezen Voor Plooifris Wasstrips?"</h2>
<div class="abs ornament" role="img" aria-label="Groot gouden bloemornament"></div>
<div class="abs features">
  <div class="feature"><div class="ico"><svg width="30" height="30" viewBox="0 0 30 30" fill="none" stroke="#c9a13c" stroke-width="1.5"><circle cx="15" cy="15" r="9"/></svg></div><div><h3>Milieuvriendelijk:</h3><p>100% biologisch afbreekbaar en plasticvrij.</p></div></div>
  <div class="feature"><div class="ico"><svg width="30" height="30" viewBox="0 0 30 30" fill="none" stroke="#c9a13c" stroke-width="1.5"><path d="M9 5l-6 5 3 4 3-2v13h12V12l3 2 3-4-6-5z"/></svg></div><div><h3>Geschikt voor Alle Stoffen:</h3><p>Veilig voor fijne was, wit, kleur en zwart.</p></div></div>
  <div class="feature"><div class="ico"><svg width="30" height="30" viewBox="0 0 30 30" fill="none" stroke="#c9a13c" stroke-width="1.5"><rect x="6" y="8" width="18" height="16" rx="2"/></svg></div><div><h3>Compact en Gebruiksvriendelijk:</h3><p>Geen gedoe met zware flessen – scheur, voeg toe en</p></div></div>
  <div class="feature"><div class="ico"><svg width="30" height="30" viewBox="0 0 30 30" fill="none" stroke="#c9a13c" stroke-width="1.5"><circle cx="15" cy="15" r="11"/><circle cx="15" cy="15" r="5"/></svg></div><div><h3>Langdurige Geur:</h3><p>Een heerlijke frisse geur die dagenlang blijft hangen.</p></div></div>
  <div class="feature"><div class="ico"><svg width="30" height="30" viewBox="0 0 30 30" fill="none" stroke="#c9a13c" stroke-width="3"><path d="M5 15l7 7 13-14"/></svg></div><div><h3>Hypoallergeen:</h3><p>Perfect voor de gevoelige huid en babykleding.</p></div></div>
  <div class="feature"><div class="ico"><svg width="34" height="30" viewBox="0 0 34 30" fill="none" stroke="#c9a13c" stroke-width="1.5"><rect x="2" y="8" width="18" height="12"/><path d="M20 11h7l4 5v4H20z"/><circle cx="8" cy="22" r="2.5"/><circle cx="26" cy="22" r="2.5"/></svg></div><div><h3>Altijd Gratis Verzending:</h3><p>Geen minimale bestelhoeveelheid vereist.</p></div></div>
</div>

<h2 class="abs section-title future-title">De Toekomst van Wassen Is Hier</h2>
<p class="abs future-text">Onze Plooifris Wasstrips combineren innovatie met duurzaamheid. Met slechts één strip per wasbeurt geniet je van een schone en heerlijk geurende was, zonder het milieu te belasten. Geen plastic flessen, geen verspilling – alleen pure waskracht in een handige strip</p>
<div class="abs product-box future-box" role="img" aria-label="Verpakking Plooifris wasstrips"></div>

<h2 class="abs section-title steps-title">Zo Gebruik Je Wasstrips</h2>
<div class="abs steps">
  <div class="step"><div class="num">01<i></i></div><p>Scheur een wasstrip af.</p></div>
  <div class="step"><div class="num">02<i></i></div><p>Plaats de strip direct in de trommel, samen met je wasgoed.</p></div>
  <div class="step"><div class="num">03<i></i></div><p>Start de wasmachine en laat de wasstrip zijn werk doen.</p></div>
  <div class="step"><div class="num">04</div><p>Plaats de strip direct in de trommel, samen met je wasgoed.</p></div>
</div>
<a class="abs btn shop-btn">Shop Nu – Vanaf €14,95"</a>

<h2 class="abs section-title reviews-title">Wat Onze Klanten Zeggen</h2>
<div class="abs review r1">
  <svg class="q" style="left:28px;top:55px" viewBox="0 0 40 30" fill="#fff"><circle cx="10" cy="20" r="8"/><circle cx="28" cy="20" r="8"/><path d="M2 20Q2 6 14 2l1 3Q8 9 8 18zM20 20Q20 6 32 2l1 3Q26 9 26 18z"/></svg>
  <blockquote>Sinds ik Plooifris gebruik, voelt mijn was frisser en luxueuzer aan dan ooit.</blockquote>
  <cite>– Lotte</cite>
  <svg class="q" style="left:348px;top:172px;transform:rotate(180deg)" viewBox="0 0 40 30" fill="#fff"><circle cx="10" cy="20" r="8"/><circle cx="28" cy="20" r="8"/><path d="M2 20Q2 6 14 2l1 3Q8 9 8 18zM20 20Q20 6 32 2l1 3Q26 9 26 18z"/></svg>
</div>
<div class="abs review r2">
  <svg class="q" style="left:28px;top:55px" viewBox="0 0 40 30" fill="#fff"><circle cx="10" cy="20" r="8"/><circle cx="28" cy="20" r="8"/><path d="M2 20Q2 6 14 2l1 3Q8 9 8 18zM20 20Q20 6 32 2l1 3Q26 9 26 18z"/></svg>
  <blockquote>Eindelijk een milieuvriendelijk product dat echt werkt en heerlijk ruikt."</blockquote>
  <cite>– Daan</cite>
  <svg class="q" style="left:348px;top:172px;transform:rotate(180deg)" viewBox="0 0 40 30" fill="#fff"><circle cx="10" cy="20" r="8"/><circle cx="28" cy="20" r="8"/><path d="M2 20Q2 6 14 2l1 3Q8 9 8 18zM20 20Q20 6 32 2l1 3Q26 9 26 18z"/></svg>
</div>

<h2 class="abs section-title faq-title">Heb Je Nog Vragen?</h2>
<div class="abs faq">
  <div class="faq-row">Zijn de wasstrips geschikt voor mensen met een gevoelige huid?<span class="plus">+</span></div>
  <div class="faq-row">Hoeveel wasbeurten bevat één verpakking?<span class="plus">+</span></div>
  <div class="faq-row">Werken de strips bij lage temperaturen?<span class="plus">+</span></div>
</div>
<a class="abs btn faq-btn">Bekijk Onze FAQ Voor Meer Antwoorden</a>

<h2 class="abs section-title cta-title">Start Vandaag Met Milieuvriendelijk<br>Wassen – Geen Plastic, Geen Gedoe.<br>Alleen Fris Wassen."</h2>
<a class="abs btn cta-btn">Bestel Nu – Maak Het Verschil!</a>

<div class="abs socials" aria-label="Sociale media">
  <span></span><b></b><span></span><b></b><span></span><b></b><span></span>
</div>
<div class="abs footer-contacts">
  <div class="contact"><svg viewBox="0 0 24 24" fill="none" stroke="#c9a13c" stroke-width="1.6"><path d="M5 3h4l2 5-2.5 1.5a11 11 0 0 0 6 6L16 13l5 2v4a2 2 0 0 1-2 2A16 16 0 0 1 3 5a2 2 0 0 1 2-2z"/></svg>+31 20 555 0142</div>
  <div class="contact"><svg viewBox="0 0 24 24" fill="none" stroke="#c9a13c" stroke-width="1.6"><rect x="2" y="5" width="20" height="14" rx="1.5"/><path d="M2 6l10 7 10-7"/></svg>info@plooifris.nl</div>
</div>
<p class="abs copyright">COPYRIGHT © 2024 <em>plooifris.nl</em></p>

</body>
</html>
```